Design a label for a dog shampoo names furbloom, the sell point of this series of shampoo is “just like wash your dogs with milk, not harm for your hand ”, the style could be gentle or professional or even amazing.

Use only 2 colors in the design job, the color of our logo could be changed, it depends on your whole page. Please design in CDR or ai.

update:
Pls do more change with the fonts when you design the front page, including title and details. Try more styles of fonts. Addition, this design will be printed on the bottle, no a label stick on it.
Updates

Do not put a real dog or animal on the page, Pay more attention to the types of fonts

Reason: Expect for more design idea.

Target Market(s)

people 20-30 years old who have dogs and cats at home

Industry/Entity Type

It Professional

Requirements
Nice to have
• It would be nice if you add some detail words in the design of the right side.

```html
<!DOCTYPE html>
<html lang="en">
<head>
<meta charset="utf-8">
<title>furbloom shampoo bottle print</title>
<link href="https://fonts.googleapis.com/css2?family=Oswald:wght@500;600&family=Tinos&family=Arimo:wght@400;700&display=swap" rel="stylesheet">
<style>
  :root{
    --teal:#47dfcc;
    --teal-soft:#c9f5ee;
    --blue:#2f7be0;
    --white:#ffffff;
    --cream:#fbf19c;
    --ink:#1c1c1c;
    --title-font:"Oswald", sans-serif;
    --serif-font:"Tinos", serif;
    --body-font:"Arimo", sans-serif;
  }
  *{box-sizing:border-box;margin:0;padding:0}
  html,body{width:1200px;height:1000px;overflow:hidden;background:var(--white)}
  .canvas{position:relative;width:1200px;height:1000px}

  /* front panels */
  .front{position:absolute;top:341px;width:171px;height:326px;overflow:hidden}
  .front .decor{position:absolute;inset:0;width:100%;height:100%}
  .front--teal{--bg:var(--teal);--side:var(--blue);--title:var(--white);--bubble:#dff9f5;--box-bg:transparent;--box-line:var(--white);--foot:var(--blue);--foot-text:var(--white)}
  .front--white{--bg:var(--white);--side:var(--teal);--title:var(--blue);--bubble:#b7f1f6;--box-bg:var(--teal);--box-line:var(--teal);--foot:var(--blue);--foot-text:var(--white)}
  .front--cream{--bg:var(--cream);--side:var(--teal);--title:var(--blue);--bubble:#fdf9d6;--box-bg:var(--teal);--box-line:var(--teal);--foot:var(--blue);--foot-text:var(--white)}

  .brand-oval{position:absolute;left:21px;top:16px;width:129px;height:73px;border-radius:50%;
    background:var(--teal);border:4px solid var(--white);display:flex;align-items:center;justify-content:center}
  .brand-name{font-family:var(--title-font);font-weight:500;font-size:21px;color:var(--white);letter-spacing:.5px}

  .product-title{position:absolute;left:0;right:0;top:112px;text-align:center;color:var(--title);
    font-family:var(--title-font);font-weight:600;font-size:14.5px;line-height:1;letter-spacing:-.2px}
  .product-title .amp{display:block;position:relative;height:11px;font-size:8px;line-height:11px}
  .product-title .amp::before{content:"";position:absolute;left:18px;right:18px;top:5px;height:2px;background:var(--title);z-index:0}
  .product-title .amp span{position:relative;z-index:1;background:var(--bg);padding:0 2px;font-family:var(--serif-font)}

  .bubbles{position:absolute;left:34px;top:168px;width:104px;height:92px;border-radius:46px;
    background:radial-gradient(circle at 40% 55%, var(--bubble) 0 35%, transparent 70%)}

  .claim-box{position:absolute;left:20px;top:257px;width:131px;height:38px;background:var(--box-bg);
    border:1.5px solid var(--box-line);display:flex;flex-direction:column;justify-content:center;
    text-align:center;font-family:var(--serif-font);font-size:10px;line-height:1.2;color:var(--white)}
  .volume{position:absolute;left:0;right:0;bottom:0;height:28px;background:var(--foot);color:var(--foot-text);
    font-family:var(--serif-font);font-weight:700;font-size:11px;display:flex;align-items:center;justify-content:center}
  .front--white .claim-box, .front--cream .claim-box{top:260px;height:34px}
  .front--white .volume, .front--cream .volume{height:24px}

  /* back panels */
  .back{position:absolute;top:341px;width:171px;height:326px;background:var(--teal);
    border-top:5px solid var(--blue);border-right:5px solid var(--blue)}
  .back .sheet{position:absolute;left:4px;top:4px;right:4px;bottom:4px;background:var(--white)}
  .back .sheet::before{content:"";position:absolute;left:0;right:0;top:90px;bottom:0;background:var(--teal-soft)}
  .back-copy{position:relative;padding:3px 5px 0;font-family:var(--body-font);font-size:5.3px;line-height:1.2;color:var(--ink);text-align:justify}
  .back-copy h3{font-size:5.6px;font-weight:400;color:var(--blue);margin-top:4px;text-transform:uppercase}
  .back-copy .lead{color:var(--blue)}
  .directions{columns:2;column-gap:6px;text-align:left}
  .directions li{list-style:none;padding-left:5px;position:relative}
  .directions li::before{content:"";position:absolute;left:0;top:1.5px;width:3px;height:3px;background:var(--blue);transform:rotate(45deg)}
  .back-foot{position:absolute;left:5px;right:5px;bottom:6px;height:40px;font-family:var(--body-font);font-size:5.6px}
  .back-foot .code{position:absolute;left:0;bottom:11px;color:var(--ink);font-weight:700}
  .back-foot .contact{position:absolute;left:0;bottom:2px;color:var(--blue)}
  .back-foot .brand-oval{left:auto;right:0;top:0;width:62px;height:38px;border-width:2px}
  .back-foot .brand-name{font-size:11px}
</style>
</head>
<body>
<main class="canvas">

  <section class="front front--teal" style="left:116px">
    <svg class="decor" viewBox="0 0 171 326" preserveAspectRatio="none" aria-hidden="true">
      <rect width="171" height="326" fill="var(--bg)"/>
      <rect x="20" y="0" width="131" height="55" fill="var(--blue)"/>
      <path d="M4,40 Q38,170 6,300 Q22,170 4,40Z" fill="var(--side)"/>
      <path d="M167,40 Q133,170 165,300 Q149,170 167,40Z" fill="var(--side)"/>
    </svg>
    <div class="brand-oval"><span class="brand-name">furbloom</span></div>
    <h2 class="product-title">SUPER-CONDITIONING<span class="amp"><span>&amp;</span></span>NUTRIENT SHAMPOO</h2>
    <div class="bubbles" role="img" aria-label="Cluster of soft milk bubbles"></div>
    <p class="claim-box"><span>MOISTURE-RICH</span><span>SMOOTH AND SILKY</span></p>
    <p class="volume">1000 ML</p>
  </section>

  <section class="front front--white" style="left:310px">
    <svg class="decor" viewBox="0 0 171 326" preserveAspectRatio="none" aria-hidden="true">
      <rect width="171" height="326" fill="var(--bg)"/>
      <rect x="14" y="0" width="143" height="40" fill="var(--blue)"/>
      <path d="M0,0 L14,0 Q14,30 22,45 Q40,170 14,300 L0,300Z" fill="var(--white)"/>
      <path d="M171,0 L157,0 Q157,30 149,45 Q131,170 157,300 L171,300Z" fill="var(--white)"/>
      <path d="M8,40 Q44,170 10,298 Q30,170 8,40Z" fill="var(--side)"/>
      <path d="M163,40 Q127,170 161,298 Q141,170 163,40Z" fill="var(--side)"/>
      <path d="M2,60 Q20,170 4,290 Q12,170 2,60Z" fill="var(--blue)"/>
      <path d="M169,60 Q151,170 167,290 Q159,170 169,60Z" fill="var(--blue)"/>
    </svg>
    <div class="brand-oval"><span class="brand-name">furbloom</span></div>
    <h2 class="product-title">SUPER-CONDITIONING<span class="amp"><span>&amp;</span></span>NUTRIENT SHAMPOO</h2>
    <div class="bubbles" role="img" aria-label="Cluster of soft milk bubbles"></div>
    <p class="claim-box"><span>MOISTURE-RICH</span><span>SMOOTH AND SILKY</span></p>
    <p class="volume">1000 ML</p>
  </section>

  <section class="front front--cream" style="left:505px">
    <svg class="decor" viewBox="0 0 171 326" preserveAspectRatio="none" aria-hidden="true">
      <rect width="171" height="326" fill="var(--bg)"/>
      <rect x="14" y="0" width="143" height="40" fill="var(--blue)"/>
      <path d="M8,40 Q44,170 10,298 Q30,170 8,40Z" fill="var(--side)"/>
      <path d="M163,40 Q127,170 161,298 Q141,170 163,40Z" fill="var(--side)"/>
      <path d="M2,60 Q20,170 4,290 Q12,170 2,60Z" fill="var(--blue)"/>
      <path d="M169,60 Q151,170 167,290 Q159,170 169,60Z" fill="var(--blue)"/>
    </svg>
    <div class="brand-oval"><span class="brand-name">furbloom</span></div>
    <h2 class="product-title">SUPER-CONDITIONING<span class="amp"><span>&amp;</span></span>NUTRIENT SHAMPOO</h2>
    <div class="bubbles" role="img" aria-label="Cluster of soft milk bubbles"></div>
    <p class="claim-box"><span>MOISTURE-RICH</span><span>SMOOTH AND SILKY</span></p>
    <p class="volume">1000 ML</p>
  </section>

  <section class="back" style="left:700px">
    <div class="sheet">
      <div class="back-copy">
        <p><span class="lead">FURBLOOM Super-Conditioning &amp; Nutrient Shampoo</span> is a specially formulated shampoo, rich in conditioners taken from milk which soften and balance the nutrition of your pet's coat. Easier and better absorbed by the coat from base to end after using. With the help of mineral ions it rinses out quickly and completely to leave a soft, sparkling and smooth coat. Safe and gentle enough to be used every day. Safe for even the most sensitive skin and coat, puppies, nursing mothers and cats.</p>
        <h3>Directions:</h3>
        <ul class="directions">
          <li>Before shampooing, brush out pet's coat.</li>
          <li>Saturate dog's coat with lukewarm water.</li>
          <li>Dispense a small amount of shampoo into the palm of your hand.</li>
          <li>To clean coat, start at dog's head and work back towards the tail. Avoid getting shampoo into the dog's eyes and ears.</li>
          <li>Rinse coat several times with lukewarm water.</li>
          <li>Towel dry and gently comb or brush coat.</li>
        </ul>
        <h3>Active ingredients:</h3>
        <p>Hypochlorous Acid, Sodium Hypochlorite</p>
        <h3>Use precautions:</h3>
        <p>Harmful if swallowed. Do not inhale. Discontinue use if irritation develops and contact your veterinarian. For animal use only. Not for human use. Keep out of reach of children. Do not decant into smaller containers. Not for injection. Always consult with a veterinarian for systemic conditions.</p>
        <h3>Storage and disposal:</h3>
        <p>Keep out of the reach of children. Replace cap. Wrap in several layers of newspaper and discard in trash.</p>
      </div>
      <div class="back-foot">
        <span class="code">BARCODE NO:</span>
        <span class="contact">Other Contact details</span>
        <div class="brand-oval"><span class="brand-name">furbloom</span></div>
      </div>
    </div>
  </section>

  <section class="back" style="left:895px">
    <div class="sheet">
      <div class="back-copy">
        <p><span class="lead">FURBLOOM Super-Conditioning &amp; Nutrient Shampoo</span> is a specially formulated shampoo, rich in conditioners taken from milk which soften and balance the nutrition of your pet's coat. Easier and better absorbed by the coat from base to end after using. With the help of mineral ions it rinses out quickly and completely to leave a soft, sparkling and smooth coat. Safe and gentle enough to be used every day. Safe for even the most sensitive skin and coat, puppies, nursing mothers and cats.</p>
        <h3>Directions:</h3>
        <ul class="directions">
          <li>Before shampooing, brush out pet's coat.</li>
          <li>Saturate dog's coat with lukewarm water.</li>
          <li>Dispense a small amount of shampoo into the palm of your hand.</li>
          <li>To clean coat, start at dog's head and work back towards the tail. Avoid getting shampoo into the dog's eyes and ears.</li>
          <li>Rinse coat several times with lukewarm water.</li>
          <li>Towel dry and gently comb or brush coat.</li>
        </ul>
        <h3>Active ingredients:</h3>
        <p>Hypochlorous Acid, Sodium Hypochlorite</p>
        <h3>Use precautions:</h3>
        <p>Harmful if swallowed. Do not inhale. Discontinue use if irritation develops and contact your veterinarian. For animal use only. Not for human use. Keep out of reach of children. Do not decant into smaller containers. Not for injection. Always consult with a veterinarian for systemic conditions.</p>
        <h3>Storage and disposal:</h3>
        <p>Keep out of the reach of children. Replace cap. Wrap in several layers of newspaper and discard in trash.</p>
      </div>
      <div class="back-foot">
        <span class="code">BARCODE NO:</span>
        <span class="contact">Other Contact details</span>
        <div class="brand-oval"><span class="brand-name">furbloom</span></div>
      </div>
    </div>
  </section>

</main>
</body>
</html>
```